"Tidewell Fellowship" needs a logo design that represents a Christian family boating ministry

Mission Statement:
“Providing compassion, care and opportunities to create memories for marginalized groups of society through ocean therapy.”
Bible verse:
Colossians 3:12 – “Therefore, as God’s chosen people, holy and dearly loved, clothe yourselves with compassion, kindness, humility, gentleness and patience.”
Target Market(s)
HOMELESS (who have gone through shelters and are on the road to recovery)
CHURCH GROUPS
INJURED MILITARY VETERANS
YOUTH AT RISK (orphans, human trafficking survivors)
SICKLY (hospitalized who can get out once in a while)
CAREGIVERS (single moms, military spouses caring for injured vets, families of those in prison)
ELDERLY (retirement centers)
SMALL BUSINESS STAFF OUTINGS
SPECIAL EVENTS
Industry/Entity Type
Ministry
Contact Information for Business Card
Captain Glen Marlowe @ 808-491-3027
Priscilla Marlowe @ 808-493-5184
info@tidewellfellowship.example
www.tidewellfellowship.example (not active yet but hopefully, soon)
Requirements
Must have
- Catch-phrase words maybe for back of business card:
- "Tide-Bound --- Kindness --- Making moments out at sea"
Nice to have
- Added 2 photo files just for visuals:
- 1 photo is of our boat.
- Other photo is our daughter's artwork on a cooler she made (for father's day gift)...might be nice and fun to incorporate daughter's artwork/inspiration into logo...but not sure if it looks to busy

```html
<!DOCTYPE html>
<html lang="en">
<head>
<meta charset="utf-8">
<title>Tidewell Fellowship – Business Card</title>
<link href="https://fonts.googleapis.com/css2?family=Open+Sans:ital,wght@0,400;0,600;0,700;1,400&display=swap" rel="stylesheet">
<style>
  :root {
    --stage: #6f6f6f;
    --navy: #2e5074;
    --sea: #1158a8;
    --white: #ffffff;
    --black: #000000;
    --hull: #34557a;
  }
  * { margin: 0; padding: 0; box-sizing: border-box; }
  html, body { width: 1200px; height: 900px; overflow: hidden; }
  body {
    background: var(--stage);
    font-family: "Open Sans", Arial, sans-serif;
    position: relative;
  }
  .card {
    position: absolute;
    top: 306px;
    width: 440px;
    height: 271px;
    border-radius: 10px;
    overflow: hidden;
  }
  .card-front { left: 149px; background: var(--navy); color: var(--white); }
  .card-back { left: 608px; background: var(--black); }

  .wave { position: absolute; left: 0; top: 0; width: 440px; height: 271px; }

  .wordmark {
    position: absolute; left: 0; right: 0;
    text-align: center; font-weight: 600;
  }
  .card-front .wordmark { top: 38px; font-size: 28px; color: var(--white); }

  .contact { position: absolute; top: 99px; }
  .contact-captain { left: 23px; }
  .contact-partner { left: 251px; }
  .contact-name { font-size: 15.5px; font-weight: 600; text-transform: uppercase; letter-spacing: 0.1px; }
  .contact-line { display: flex; align-items: center; gap: 5px; font-size: 12.5px; line-height: 17px; }
  .contact-line svg { width: 10px; height: 10px; fill: var(--white); flex: none; }

  .online { position: absolute; left: 23px; top: 144px; }

  .verse {
    position: absolute; left: 0; right: 0; top: 228px;
    text-align: center; font-style: italic; font-size: 10px; line-height: 14px;
  }

  .emblem {
    position: absolute; left: 100px; top: 88px;
    width: 240px; height: 75px; border-radius: 4px;
    background: linear-gradient(180deg, var(--hull) 0%, var(--sea) 100%);
  }
  .card-back .wordmark { top: 172px; font-size: 34px; color: var(--hull); }
  .tagline {
    position: absolute; left: 0; right: 0; top: 227px;
    text-align: center; font-style: italic; font-size: 12.5px; color: var(--white);
  }
</style>
</head>
<body>
  <section class="card card-front">
    <svg class="wave" viewBox="0 0 440 271" aria-hidden="true">
      <path d="M0 199 C120 186 230 176 310 186 C370 193 410 208 440 224 L440 271 L0 271 Z" fill="var(--sea)"/>
    </svg>
    <div class="wordmark">Tidewell Fellowship</div>

    <div class="contact contact-captain">
      <div class="contact-name">Captain Glen Marlowe</div>
      <div class="contact-line">
        <svg viewBox="0 0 10 10"><path d="M2 0.5 L3.6 2.6 L2.8 3.6 C3.4 5 4.8 6.4 6.3 7.1 L7.3 6.3 L9.5 8 L8.4 9.5 C4.5 9.2 0.8 5.5 0.5 1.6 Z"/></svg>
        <span>808-491-3027</span>
      </div>
    </div>
    <div class="contact contact-partner">
      <div class="contact-name">Priscilla Marlowe</div>
      <div class="contact-line">
        <svg viewBox="0 0 10 10"><path d="M2 0.5 L3.6 2.6 L2.8 3.6 C3.4 5 4.8 6.4 6.3 7.1 L7.3 6.3 L9.5 8 L8.4 9.5 C4.5 9.2 0.8 5.5 0.5 1.6 Z"/></svg>
        <span>808-493-5184</span>
      </div>
    </div>

    <div class="online">
      <div class="contact-line">
        <svg viewBox="0 0 10 10"><path d="M0.5 2 H9.5 V8.5 H0.5 Z M1 2.4 L5 5.6 L9 2.4" stroke="var(--navy)" stroke-width="0.8"/></svg>
        <span>info@tidewellfellowship.example</span>
      </div>
      <div class="contact-line">
        <svg viewBox="0 0 10 10"><circle cx="5" cy="5" r="4.5"/><path d="M0.5 5 H9.5 M5 0.5 C3 3 3 7 5 9.5 M5 0.5 C7 3 7 7 5 9.5" stroke="var(--navy)" stroke-width="0.7" fill="none"/></svg>
        <span>www.tidewellfellowship.example</span>
      </div>
    </div>

    <p class="verse">Therefore, as God’s chosen people, holy and dearly loved, clothe yourselves<br>with compassion, kindness, humility, gentleness and patience. - Colossians 3:12</p>
  </section>

  <section class="card card-back">
    <div class="emblem" role="img" aria-label="Illustration of a motor boat on waves with a leaping dolphin"></div>
    <div class="wordmark">Tidewell Fellowship</div>
    <p class="tagline">Tide-Bound | Kindness | Making moments out at sea</p>
  </section>
</body>
</html>
```